Financial Planning Firm needs a client data collection summary sheet to print on A3

We are a financial advice company, and we are after a 1-page sheet where we can write all of the client’s personal information in our meetings, like a mind map.
It should have our logo on the page along with a place to put the Client's Name and the Date.
It also needs to have the following Headings
Family
Home
Investments
Business
Estate Plan
Lifestyle
Money
Retirement
Dreams & Goals
Health and Wellbeing
It also needs to have our License details on the bottom: Tellora Counsel Pty Ltd (538216) is an Authorised Representative of Brindle Estate Capital Group Pty Ltd AFSL No: 613985 ABN 57 218 964 402. This document has been prepared by Tellora Counsel and is for general information only.
Please utilise our colour scheme as per our logo attached. Please find uploaded to the project an example data collection summary sheet that we use currently.

```html
<!DOCTYPE html>
<html lang="en">
<head>
<meta charset="utf-8">
<title>Tellora Counsel – Personal Information Form</title>
<link rel="stylesheet" href="https://fonts.googleapis.com/css2?family=Montserrat:wght@400;500&family=PT+Sans:ital,wght@0,400;0,700;1,700&display=swap">
<style>
  :root {
    --backdrop: #ecebe9;
    --paper: #ffffff;
    --paper-edge: #f3f3f4;
    --ink: #111111;
    --rule: #2a2a2a;
    --gold: #c9a270;
    --gold-light: #e6cfa8;
    --band-dark: #0d0d0d;
    --band-white: #ffffff;
  }
  * { box-sizing: border-box; margin: 0; padding: 0; }
  html, body {
    width: 1200px; height: 784px; overflow: hidden;
    background: var(--backdrop);
  }
  .sheet {
    position: absolute; left: 322px; top: 10px;
    width: 556px; height: 764px;
    background: var(--paper);
    box-shadow: 0 2px 8px rgba(0,0,0,.12);
    font-family: "PT Sans", Arial, sans-serif;
    color: var(--ink);
    overflow: hidden;
  }
  .corner-bar {
    position: absolute; height: 9px; width: 62px;
    background: linear-gradient(90deg, var(--gold), var(--gold-light));
  }
  .corner-bar--tl { left: 0; top: 14px; clip-path: polygon(0 0, 100% 0, 86% 100%, 0 100%); }
  .corner-bar--tr { right: 0; top: 14px; clip-path: polygon(0 0, 100% 0, 100% 100%, 14% 100%); }
  .corner-bar--bl { left: 0; bottom: 10px; clip-path: polygon(0 0, 86% 0, 100% 100%, 0 100%); }
  .corner-bar--br { right: 0; bottom: 10px; clip-path: polygon(14% 0, 100% 0, 100% 100%, 0 100%); }

  .header { position: absolute; left: 0; top: 0; width: 100%; height: 78px; }
  .field-name { position: absolute; left: 40px; top: 34px; font-size: 7px; font-style: italic; }
  .field-name .box { display: block; margin-top: 2px; width: 120px; height: 12px; border: 1px solid var(--rule); }
  .brand { position: absolute; left: 0; right: 0; top: 12px; text-align: center; }
  .brand-name {
    font-family: "Montserrat", Arial, sans-serif; font-weight: 500;
    font-size: 19px; letter-spacing: 3px; text-transform: uppercase;
  }
  .brand-tagline {
    margin-top: 3px; font-family: "Montserrat", Arial, sans-serif; font-weight: 400;
    font-size: 6.5px; letter-spacing: 3px; text-transform: uppercase;
  }
  .brand-tagline::before, .brand-tagline::after {
    content: ""; display: inline-block; width: 24px; height: 1px; background: var(--ink);
    vertical-align: middle; margin: 0 8px;
  }
  .form-title {
    margin-top: 4px; font-family: "Montserrat", Arial, sans-serif; font-weight: 500;
    font-size: 5.5px; letter-spacing: 2.2px; text-transform: uppercase;
  }
  .field-date { position: absolute; right: 36px; top: 34px; font-size: 7px; font-style: italic; text-align: right; }
  .date-boxes { display: flex; margin-top: 2px; }
  .date-boxes span { width: 12px; height: 12px; border: 1px solid var(--rule); margin-left: -1px; }

  .sections { position: absolute; left: 28px; right: 28px; top: 70px; }
  .section { height: 64px; }
  .band {
    height: 14px; margin: 0 -28px;
    background: linear-gradient(180deg, var(--band-white) 0%, #7a7a7a 25%, var(--band-dark) 50%, #7a7a7a 75%, var(--band-white) 100%);
    display: flex; align-items: center; justify-content: center;
    border-bottom: 1px solid var(--gold);
  }
  .band-title { color: #fff; font-weight: 700; font-style: italic; font-size: 9.5px; letter-spacing: .2px; }
  .section--lead .band { background: linear-gradient(180deg, var(--band-white) 0%, #7a7a7a 25%, var(--band-dark) 50%, #7a7a7a 75%, var(--band-white) 100%); }
  .write-line { height: 12.25px; border-bottom: 0.7px solid var(--rule); }

  .footer { position: absolute; left: 0; right: 0; bottom: 4px; text-align: center; }
  .footer-name { font-weight: 700; font-size: 7.5px; }
  .footer-star { font-size: 6px; line-height: 7px; }
  .footer-licence { font-size: 5px; line-height: 6px; padding: 0 70px; }
</style>
</head>
<body>
  <main class="sheet">
    <div class="corner-bar corner-bar--tl"></div>
    <div class="corner-bar corner-bar--tr"></div>
    <div class="corner-bar corner-bar--bl"></div>
    <div class="corner-bar corner-bar--br"></div>

    <header class="header">
      <div class="field-name">Name<span class="box"></span></div>
      <div class="brand">
        <div class="brand-name">Tellora Counsel</div>
        <div class="brand-tagline">Your Financial Expert</div>
        <div class="form-title">Personal Information Form</div>
      </div>
      <div class="field-date">SOC Date
        <div class="date-boxes"><span></span><span></span><span></span><span></span><span></span><span></span></div>
      </div>
    </header>

    <section class="sections">
      <div class="section"><div class="band"><span class="band-title">Family</span></div><div class="write-line"></div><div class="write-line"></div><div class="write-line"></div><div class="write-line"></div></div>
      <div class="section"><div class="band"><span class="band-title">Home</span></div><div class="write-line"></div><div class="write-line"></div><div class="write-line"></div><div class="write-line"></div></div>
      <div class="section"><div class="band"><span class="band-title">Investments</span></div><div class="write-line"></div><div class="write-line"></div><div class="write-line"></div><div class="write-line"></div></div>
      <div class="section"><div class="band"><span class="band-title">Business</span></div><div class="write-line"></div><div class="write-line"></div><div class="write-line"></div><div class="write-line"></div></div>
      <div class="section"><div class="band"><span class="band-title">Estate Plan</span></div><div class="write-line"></div><div class="write-line"></div><div class="write-line"></div><div class="write-line"></div></div>
      <div class="section"><div class="band"><span class="band-title">Lifestyle</span></div><div class="write-line"></div><div class="write-line"></div><div class="write-line"></div><div class="write-line"></div></div>
      <div class="section"><div class="band"><span class="band-title">Money</span></div><div class="write-line"></div><div class="write-line"></div><div class="write-line"></div><div class="write-line"></div></div>
      <div class="section"><div class="band"><span class="band-title">Retirement</span></div><div class="write-line"></div><div class="write-line"></div><div class="write-line"></div><div class="write-line"></div></div>
      <div class="section"><div class="band"><span class="band-title">Dreams &amp; Goals</span></div><div class="write-line"></div><div class="write-line"></div><div class="write-line"></div><div class="write-line"></div></div>
      <div class="section"><div class="band"><span class="band-title">Health and Wellbeing</span></div><div class="write-line"></div><div class="write-line"></div><div class="write-line"></div><div class="write-line"></div></div>
    </section>

    <footer class="footer">
      <div class="footer-name">Tellora Counsel Pty Ltd</div>
      <div class="footer-star">★</div>
      <p class="footer-licence">(538216) is an Authorised Representative of Brindle Estate Capital Group Pty Ltd AFSL No: 613985 ABN 57 218 964 402. This document has been prepared by Tellora Counsel and is for general information only.</p>
    </footer>
  </main>
</body>
</html>
```